Electrical company needs a brochure designed for electrical construction work

we need a brochure designed for our company BRONZEWAY ELECTRICAL INSTALLATIONS. we are a group of electricians working in the construction industry delivering electrical constructon services to builders and other clients in the commercial and Industrial working environments. we would like our logo to stand out with a dark theme and also give a professional fee.l we have a brief description of what we do and our experiences in a word doc i will provide it along with our logo design

Target Market(s)

builders for commercial and industrial construction projects

Industry/Entity Type

Electric Company

Font styles to use
Serif

Colors
0456a4
96b7d9
5c5c5c
757575
000000
aaaaaa
ec1f27
33a6d7
0493ce

Requirements
Must have
• a professional feel,
Nice to have
• some wording that makes us stand out and brings all the attention

```html
<!DOCTYPE html>
<html lang="en">
<head>
<meta charset="utf-8">
<title>Bronzeway Electrical Installations – Brochure Outside</title>
<link rel="stylesheet" href="https://fonts.googleapis.com/css2?family=Montserrat:wght@400;500;700;800&display=swap">
<style>
  :root {
    --page-bg: #e9e9e9;
    --cover-dark: #1b1b1d;
    --cover-mid: #232326;
    --fold-line: #141416;
    --faint-type: #262629;
    --brand-blue: #33a6d7;
    --accent-red: #ec1f27;
    --text-light: #d8d8d8;
    --text-muted: #aaaaaa;
  }
  * { margin: 0; padding: 0; box-sizing: border-box; }
  html, body { width: 902px; height: 1200px; overflow: hidden; }
  body {
    background: var(--page-bg);
    font-family: "Montserrat", sans-serif;
    position: relative;
  }
  .brochure-spread {
    position: absolute;
    left: 21px; top: 322px;
    width: 860px; height: 555px;
    background: linear-gradient(135deg, var(--cover-mid), var(--cover-dark) 60%);
    box-shadow: 0 14px 24px rgba(0,0,0,0.28);
    overflow: hidden;
  }
  .fold {
    position: absolute; left: 430px; top: 0;
    width: 2px; height: 100%;
    background: var(--fold-line);
    opacity: 0.6;
  }
  .map-area {
    position: absolute; left: 40px; top: 40px;
    width: 780px; height: 420px;
    background: radial-gradient(ellipse at 45% 40%, rgba(60,60,64,0.35), rgba(27,27,29,0) 70%);
  }
  .back-watermark {
    position: absolute;
    left: 40px; top: 520px;
    transform: rotate(-90deg);
    transform-origin: left top;
    font-weight: 800;
    font-size: 34px;
    letter-spacing: 2px;
    color: var(--faint-type);
    white-space: nowrap;
  }
  .contact-block {
    position: absolute;
    left: 116px; top: 475px;
    width: 200px;
    text-align: center;
    font-size: 7.5px;
    line-height: 1.55;
    color: var(--text-light);
  }
  .contact-name {
    font-size: 11px;
    color: var(--accent-red);
    letter-spacing: 0.2px;
  }
  .front-brand {
    position: absolute;
    left: 496px; top: 282px;
    display: flex; align-items: center; gap: 12px;
  }
  .brand-dot {
    width: 34px; height: 34px;
    border-radius: 50%;
    background: var(--brand-blue);
    flex: none;
  }
  .brand-name {
    font-weight: 700;
    font-size: 17px;
    line-height: 1.15;
    color: var(--brand-blue);
    letter-spacing: 0.5px;
  }
  .website {
    position: absolute;
    left: 575px; top: 513px;
    font-size: 9px;
    letter-spacing: 2.4px;
    color: var(--text-muted);
  }
</style>
</head>
<body>
  <section class="brochure-spread" aria-label="Brochure outside spread">
    <div class="map-area" role="img" aria-label="Faint world map texture across the cover"></div>
    <div class="fold"></div>

    <div class="back-watermark">BRONZEWAY ELECTRICAL INSTALLATIONS</div>

    <div class="contact-block">
      <div class="contact-name">DALE WHITCOMBE</div>
      <div>Bronzeway Electrical Installations</div>
      <div>0400 555 172</div>
      <div>office@bronzeway.example</div>
    </div>

    <div class="front-brand">
      <span class="brand-dot"></span>
      <div class="brand-name">BRONZEWAY<br>ELECTRICAL INSTALLATIONS</div>
    </div>

    <div class="website">www.bronzeway.example</div>
  </section>
</body>
</html>
```